Business Card Design

No logos or construction designs

Easy to read Ray Tolliver Roofing, LLC (in red)

all other lettering in black I guess I am open to what the designers come up

Industry/Entity Type

Construction

Contact Information for Business Card

Ray Tolliver Roofing, LLC office 555-2189063 fax 555-318-940 3075 Marrowfield W Massillon, Ohio 40000
Ray@RayTolliverRoofing.example Residential Commerical
Ray Tolliver cell 555-862-1375

```html
<!DOCTYPE html>
<html lang="en">
<head>
<meta charset="utf-8">
<title>Ray Tolliver Roofing, LLC – Business Card</title>
<link href="https://fonts.googleapis.com/css2?family=Arimo:wght@400;700&display=swap" rel="stylesheet">
<style>
  :root {
    --backdrop: #2b2b2b;
    --card: #fbfbfb;
    --red: #e8151d;
    --ink: #1a1a1a;
    --rule: #222222;
  }
  * { margin: 0; padding: 0; box-sizing: border-box; }
  html, body {
    width: 1200px; height: 900px; overflow: hidden;
    background: var(--backdrop);
    font-family: "Arimo", Arial, sans-serif;
  }
  .business-card {
    position: absolute;
    left: 150px; top: 193px;
    width: 900px; height: 514px;
    background: var(--card);
    color: var(--ink);
    overflow: hidden;
  }
  .brand-name {
    position: absolute; left: 38px; top: 28px;
    font-size: 104px; font-weight: 700; color: var(--red);
    line-height: 1; letter-spacing: -1px; white-space: nowrap;
  }
  .brand-suffix {
    position: absolute; left: 548px; top: 140px;
    font-size: 40px; font-weight: 400; color: var(--red);
    white-space: nowrap;
  }
  .divider {
    position: absolute; height: 2px; background: var(--rule);
  }
  .divider-left { left: 0; top: 212px; width: 500px; }
  .divider-right { left: 838px; top: 262px; width: 62px; }
  .address-block {
    position: absolute; left: 38px; top: 250px;
    font-size: 25px; line-height: 1.25; letter-spacing: 0.5px;
  }
  .address-label { color: var(--red); }
  .contact-person {
    position: absolute; left: 518px; top: 200px; white-space: nowrap;
  }
  .person-name {
    font-size: 32px; font-weight: 700; color: var(--red); letter-spacing: 1px;
  }
  .person-services { font-size: 29px; margin-top: 4px; }
  .contact-list {
    position: absolute; left: 490px; top: 318px; list-style: none;
    font-size: 24px; letter-spacing: 1px;
  }
  .contact-item {
    display: flex; align-items: center; gap: 18px; height: 31px; white-space: nowrap;
  }
  .contact-item svg { width: 24px; height: 24px; flex: none; }
  .contact-email { font-size: 20px; letter-spacing: 0.2px; }
  .accent-band {
    position: absolute; top: 452px; height: 44px; background: var(--red);
  }
  .accent-band-left { left: 0; width: 470px; top: 456px; height: 40px; }
  .accent-band-right { left: 478px; right: 0; }
</style>
</head>
<body>
  <div class="business-card">
    <div class="brand-name">Ray Tolliver</div>
    <div class="brand-suffix">Roofing, LLC</div>

    <div class="divider divider-left"></div>
    <div class="divider divider-right"></div>

    <div class="address-block">
      <div class="address-label">Company address:</div>
      <div>3075 Marrowfield W Massillon,</div>
      <div>Ohio 40000</div>
    </div>

    <div class="contact-person">
      <div class="person-name">RAY TOLLIVER</div>
      <div class="person-services">Residential Commerical</div>
    </div>

    <ul class="contact-list">
      <li class="contact-item">
        <svg viewBox="0 0 24 24" aria-label="Cell">
          <rect x="1" y="1" width="22" height="22" fill="var(--red)"/>
          <rect x="8" y="4" width="8" height="16" rx="1.5" fill="none" stroke="#fff" stroke-width="1.6"/>
          <circle cx="12" cy="17" r="1" fill="#fff"/>
        </svg>
        <span>555-862-1375</span>
      </li>
      <li class="contact-item">
        <svg viewBox="0 0 24 24" aria-label="Office">
          <rect x="1" y="1" width="22" height="22" fill="var(--red)"/>
          <path d="M8 5c-2 1-3 3-1 7s5 7 8 7c1 0 2-1 2-2l-2-2-2 1c-2-1-3-3-4-5l1-2-2-4z" fill="#fff"/>
        </svg>
        <span>555-2189063</span>
      </li>
      <li class="contact-item">
        <svg viewBox="0 0 24 24" aria-label="Fax">
          <rect x="1" y="1" width="22" height="22" fill="var(--red)"/>
          <rect x="8" y="4" width="8" height="5" fill="none" stroke="#fff" stroke-width="1.5"/>
          <rect x="5" y="9" width="14" height="7" fill="none" stroke="#fff" stroke-width="1.5"/>
          <rect x="8" y="14" width="8" height="6" fill="#fff"/>
        </svg>
        <span>555-318-940</span>
      </li>
      <li class="contact-item">
        <svg viewBox="0 0 24 24" aria-label="Email">
          <rect x="1" y="1" width="22" height="22" fill="var(--red)"/>
          <rect x="4" y="6.5" width="16" height="11" fill="none" stroke="#fff" stroke-width="1.5"/>
          <path d="M4 6.5l8 6 8-6" fill="none" stroke="#fff" stroke-width="1.5"/>
        </svg>
        <span class="contact-email">Ray@RayTolliverRoofing.example</span>
      </li>
    </ul>

    <div class="accent-band accent-band-left"></div>
    <div class="accent-band accent-band-right"></div>
  </div>
</body>
</html>
```